Chiropractic Software Company needs Business Cards

We need a bushiness card design for use at a Chiropractic conference. We build billing, practice management, and medical documentation software. Our product is Vantora Chiropractic Software(Vantora for short). On top of our software we have practice success coaches that coordinate with our chiropractor clients to help them grow their practice and treat more patients. Our logo colors are tried-and-true orange-and-blue. We'd like a sterile white background and a clean layout; organizing the following information: Name, Position/Title, Phone Number, Address, email, and our website. On the backside we'd like our Logo and our slogan, "Your Clinic Keel" and our website(http://www.vantorachiropracticsoftware.example)

Industry/Entity Type

Business

```html
<!DOCTYPE html>
<html lang="en">
<head>
<meta charset="utf-8">
<title>Vantora Chiropractic Software – Business Card</title>
<link rel="stylesheet" href="https://fonts.googleapis.com/css2?family=Arimo:wght@400;700&display=swap">
<style>
  :root {
    --bg: #e9e9e9;
    --card: #ffffff;
    --blue: #1a5fae;
    --band-blue: #1f7ac4;
    --orange: #ee6a24;
    --edge: #c9c9c9;
  }
  * { margin: 0; padding: 0; box-sizing: border-box; }
  html, body { width: 1200px; height: 1000px; overflow: hidden; }
  body {
    background: var(--bg);
    font-family: "Arimo", Arial, sans-serif;
    position: relative;
  }
  .card {
    position: absolute;
    top: 341px;
    width: 540px;
    height: 318px;
    background: var(--card);
    border: 1px solid var(--edge);
    overflow: hidden;
  }
  .card--front { left: 40px; }
  .card--back { left: 620px; }

  .holder { position: absolute; left: 298px; top: 32px; }
  .holder__name { color: var(--orange); font-weight: 700; font-size: 21px; letter-spacing: 0.3px; }
  .holder__title { color: var(--blue); font-size: 14px; margin-top: 3px; }

  .brand { display: flex; align-items: center; gap: 10px; }
  .brand__dot { border-radius: 50%; background: var(--orange); flex: none; }
  .brand__name { color: var(--blue); font-weight: 700; }

  .card--front .brand { position: absolute; left: 57px; top: 108px; }
  .card--front .brand__dot { width: 22px; height: 22px; }
  .card--front .brand__name { font-size: 30px; }

  .contact { position: absolute; left: 57px; top: 174px; color: var(--blue); font-size: 14.5px; line-height: 18.5px; }
  .contact__row { display: flex; align-items: center; gap: 6px; }
  .contact__icon { width: 12px; height: 12px; flex: none; }
  .contact__address { margin-top: 3px; }

  .band { position: absolute; left: 0; bottom: 0; width: 100%; height: 27px; }

  .back-stack {
    position: absolute;
    left: 0; right: 0; top: 62px;
    display: flex;
    flex-direction: column;
    align-items: center;
  }
  .card--back .brand { gap: 18px; }
  .card--back .brand__dot { width: 52px; height: 52px; }
  .card--back .brand__name { font-size: 74px; line-height: 1.1; }
  .slogan {
    margin-top: 22px;
    color: var(--orange);
    font-weight: 700;
    font-size: 22px;
    letter-spacing: 0.4px;
  }
  .website {
    margin-top: 10px;
    color: var(--blue);
    font-size: 15px;
  }
</style>
</head>
<body>
  <section class="card card--front" aria-label="Business card front">
    <div class="holder">
      <p class="holder__name">Marten Halloway</p>
      <p class="holder__title">Director</p>
    </div>

    <div class="brand">
      <span class="brand__dot"></span>
      <span class="brand__name">Vantora</span>
    </div>

    <div class="contact">
      <p class="contact__row">
        <svg class="contact__icon" viewBox="0 0 12 12" aria-hidden="true"><path d="M3 1 L5 3.5 L4 5 Q5 7.5 7 8 L8.5 7 L11 9 L9.5 11 Q3 10.5 1 3 Z" fill="var(--orange)"/></svg>
        +41 00 555 01 27
      </p>
      <p class="contact__row">
        <svg class="contact__icon" viewBox="0 0 12 12" aria-hidden="true"><rect x="1" y="3" width="10" height="7.5" rx="1" fill="var(--orange)"/><path d="M1.5 3.5 L6 7 L10.5 3.5" stroke="#fff" stroke-width="1" fill="none"/></svg>
        info@vantoraclinic.example
      </p>
      <p class="contact__row">
        <svg class="contact__icon" viewBox="0 0 12 12" aria-hidden="true"><circle cx="6" cy="6" r="5" fill="none" stroke="var(--orange)" stroke-width="1.3"/><ellipse cx="6" cy="6" rx="2.2" ry="5" fill="none" stroke="var(--orange)" stroke-width="1"/><path d="M1 6 H11 M2 3.5 H10 M2 8.5 H10" stroke="var(--orange)" stroke-width="0.9"/></svg>
        www.vantorachiropracticsoftware.example
      </p>
      <p class="contact__address">Rue des Tilleuls 14, City Name<br>PO BOX 2048, Country</p>
    </div>

    <svg class="band" viewBox="0 0 540 27" preserveAspectRatio="none" aria-hidden="true">
      <polygon points="0,0 347,0 337,27 0,27" fill="var(--band-blue)"/>
      <polygon points="355,0 540,0 540,27 345,27" fill="var(--orange)"/>
    </svg>
  </section>

  <section class="card card--back" aria-label="Business card back">
    <div class="back-stack">
      <div class="brand">
        <span class="brand__dot"></span>
        <span class="brand__name">Vantora</span>
      </div>
      <p class="slogan">Your Clinic Keel</p>
      <p class="website">www.vantorachiropracticsoftware.example</p>
    </div>
  </section>
</body>
</html>
```